Breast Cancer Stickers

Hi,
i would like a of small design for a breast cancer awareness campaign. please check attached picture this is the size and font i want. these will be stickers. Then i would like a little pink ribbon after each dot. so there will be four design please find below colors, slogans, etc..
1 I PINK I CAN. (Off white Background, Light Pink Font)
Never give up.
2 PINK POWER. (Black Background, Bright Pink Font)
Theres Always hope
3 POSITIVELY PINK. ( Light Pink Background, Off white Font)
Stay Positive
4 TURN UP THE PINK. (Bright Pink Background, Black font)
fight on.
Campaign

```html
<!DOCTYPE html>
<html lang="en">
<head>
<meta charset="utf-8">
<title>Breast Cancer Awareness Stickers</title>
<link rel="stylesheet" href="https://fonts.googleapis.com/css2?family=Inter:wght@700&display=swap">
<style>
  :root {
    --off-white: #dedad6;
    --light-pink: #ea90bb;
    --soft-pink-text: #f08cb4;
    --bright-pink: #ec008c;
    --black: #231f20;
    --grey-text: #58595b;
    --white: #ffffff;
    --page: #ffffff;
  }
  * { margin: 0; padding: 0; box-sizing: border-box; }
  html, body {
    width: 1200px;
    height: 1000px;
    overflow: hidden;
    background: var(--page);
  }
  .sheet {
    position: relative;
    width: 1200px;
    height: 1000px;
    font-family: "Inter", "Helvetica Neue", Arial, sans-serif;
    font-weight: 700;
  }
  .sticker {
    position: absolute;
    width: 459px;
    height: 459px;
    box-shadow: 0 4px 14px rgba(0, 0, 0, 0.18);
  }
  .sticker--pink-can { left: 114px; top: 26px; background: var(--off-white); }
  .sticker--pink-power { left: 613px; top: 26px; background: var(--black); }
  .sticker--turn-up { left: 109px; top: 506px; width: 463px; height: 463px; background: var(--bright-pink); }
  .sticker--positively { left: 612px; top: 506px; background: var(--light-pink); }

  .sticker__content {
    position: absolute;
    left: 49px;
  }
  .sticker--pink-can .sticker__content,
  .sticker--pink-power .sticker__content { top: 104px; }
  .sticker--turn-up .sticker__content { top: 88px; }
  .sticker--positively .sticker__content { top: 106px; left: 48px; }

  .slogan {
    font-size: 86px;
    line-height: 76px;
    letter-spacing: -2.5px;
    white-space: nowrap;
  }
  .sticker--turn-up .slogan { line-height: 80px; }
  .tagline {
    font-size: 24px;
    line-height: 28px;
    letter-spacing: -0.2px;
    margin-top: 22px;
  }
  .sticker--turn-up .tagline { margin-top: 18px; }
  .sticker--positively .tagline { margin-top: 12px; }

  .sticker--pink-can .slogan { color: var(--soft-pink-text); }
  .sticker--pink-can .tagline { color: var(--grey-text); }
  .sticker--pink-power .slogan { color: var(--bright-pink); }
  .sticker--pink-power .tagline { color: var(--white); }
  .sticker--turn-up .slogan { color: var(--black); }
  .sticker--turn-up .tagline { color: var(--off-white); }
  .sticker--positively .slogan { color: var(--off-white); }
  .sticker--positively .tagline { color: var(--black); }

  .ribbon {
    display: inline-block;
    width: 38px;
    height: 66px;
    margin-left: 4px;
    vertical-align: -8px;
  }
  .ribbon path {
    fill: none;
    stroke: currentColor;
    stroke-width: 6;
    stroke-linecap: round;
  }
  .sticker--pink-can .ribbon { color: var(--bright-pink); }
  .sticker--pink-power .ribbon { color: var(--soft-pink-text); }
  .sticker--turn-up .ribbon { color: var(--white); }
  .sticker--positively .ribbon { color: var(--bright-pink); }
</style>
</head>
<body>
<main class="sheet">

  <section class="sticker sticker--pink-can">
    <div class="sticker__content">
      <p class="slogan">I pink<br>I can.<svg class="ribbon" viewBox="0 0 40 66" aria-hidden="true"><path d="M14 8 C 16 0, 24 0, 26 8"/><path d="M14 8 C 12 22, 22 36, 34 62"/><path d="M26 8 C 28 22, 18 36, 6 62"/></svg></p>
      <p class="tagline">Never give up.</p>
    </div>
  </section>

  <section class="sticker sticker--pink-power">
    <div class="sticker__content">
      <p class="slogan">Pink<br>power.<svg class="ribbon" viewBox="0 0 40 66" aria-hidden="true"><path d="M14 8 C 16 0, 24 0, 26 8"/><path d="M14 8 C 12 22, 22 36, 34 62"/><path d="M26 8 C 28 22, 18 36, 6 62"/></svg></p>
      <p class="tagline">There’s always hope.</p>
    </div>
  </section>

  <section class="sticker sticker--turn-up">
    <div class="sticker__content">
      <p class="slogan">Turn<br>up the<br>pink.<svg class="ribbon" viewBox="0 0 40 66" aria-hidden="true"><path d="M14 8 C 16 0, 24 0, 26 8"/><path d="M14 8 C 12 22, 22 36, 34 62"/><path d="M26 8 C 28 22, 18 36, 6 62"/></svg></p>
      <p class="tagline">Fight on.</p>
    </div>
  </section>

  <section class="sticker sticker--positively">
    <div class="sticker__content">
      <p class="slogan">Positively<br>pink.<svg class="ribbon" viewBox="0 0 40 66" aria-hidden="true"><path d="M14 8 C 16 0, 24 0, 26 8"/><path d="M14 8 C 12 22, 22 36, 34 62"/><path d="M26 8 C 28 22, 18 36, 6 62"/></svg></p>
      <p class="tagline">Stay positive.</p>
    </div>
  </section>

</main>
</body>
</html>
```